Wordpress Design Project - QuorvanLabs

I would like our existing old website at www.quorvanlabs.example to be redesigned to a more modern attractive site using Wordpress, a total of 5 web pages. And also installed onto our new web hosting site. Please visit the existing website using Microsoft Internet explorer to see the content.
The new site must be compatible with all popular web browsers and mobile devices (if possible).
There should be a contact button available on each page with an associated form in case an interested person wants to contact us. This form must be spam proof not allowing automated crawlers from activating it.
Updates

There are only 5 pages web pages to this QuorvanLabs project.

Industry/Entity Type

Internet

```html
<!DOCTYPE html>
<html lang="en">
<head>
<meta charset="utf-8">
<title>QuorvanLabs – Telephone VoIP Solutions</title>
<link href="https://fonts.googleapis.com/css2?family=Arimo:wght@400;700&display=swap" rel="stylesheet">
<style>
:root{
  --page:#e6e6e6;
  --blue:#0a5aa4;
  --blue-dark:#064a8c;
  --link:#0b4d8c;
  --heading:#4a4a4a;
  --text:#555;
  --white:#fff;
  --dark:#3a3a3a;
  --darker:#222;
  --line:#e3e3e3;
  --field:#d4d4d4;
  --red:#8c0b0b;
}
*{box-sizing:border-box;margin:0;padding:0}
html,body{width:1174px;height:1200px;overflow:hidden}
body{background:var(--page);font-family:"Arimo",Arial,sans-serif;color:var(--text);position:relative}
.stage{position:absolute;left:0;top:0;width:1150px;height:1175px;transform:scale(1.0209);transform-origin:0 0}
.abs{position:absolute}
.band{left:0;top:104px;width:1150px;height:98px;background:linear-gradient(var(--blue),var(--blue-dark))}
.header{left:86px;top:17px;width:978px;height:110px;background:var(--white);border-radius:5px;box-shadow:0 1px 3px rgba(0,0,0,.15)}
.brand{left:97px;top:30px;display:flex;align-items:center;gap:14px}
.brand-mark{width:56px;height:56px;border-radius:50%;background:var(--blue)}
.brand-name{font-size:30px;font-weight:700;color:var(--blue)}
.contact-btn{left:860px;top:32px;width:196px;height:34px;border-radius:4px;background:linear-gradient(#6a6a6a,#333);color:#fff;font-size:13px;font-weight:700;letter-spacing:.5px;display:flex;align-items:center;padding-left:66px;box-shadow:0 2px 3px rgba(0,0,0,.3)}
.contact-btn svg{position:absolute;left:6px;top:-2px}
.callus{right:94px;top:95px;font-size:14px;color:#666;white-space:nowrap}
.callus b{color:var(--blue);font-size:15px}
.callus a{color:var(--blue);text-decoration:none}
.nav{left:99px;top:135px;display:flex;height:42px}
.nav a{color:#fff;font-size:13px;font-weight:700;text-decoration:none;display:flex;align-items:center;padding:0 24px;margin-right:12px}
.nav a.active{background:#fff;color:#333;border-radius:4px 4px 0 0}
.main{left:86px;top:177px;width:978px;height:910px;background:#fff;border-radius:0 0 5px 5px;box-shadow:0 1px 3px rgba(0,0,0,.15)}
.slider{left:95px;top:187px;width:962px;height:288px;background:linear-gradient(90deg,#e9e9e9,#f7f7f7 60%,#ececec);border:2px solid #e0e0e0;border-radius:3px;overflow:hidden}
.slide-photo{left:0;top:0;width:530px;height:284px;background:linear-gradient(90deg,#d9d4cf,#ece8e4 60%,rgba(247,247,247,0))}
.slide-art{left:636px;top:18px;width:210px;height:140px;border-radius:8px;background:radial-gradient(circle at 50% 50%,#b7c4d4,#dfe4ea 70%,rgba(247,247,247,0))}
.slide-text{right:16px;top:172px;text-align:right;font-size:17.5px;font-weight:700;color:#4a4a4a;line-height:28px}
.dots{left:838px;top:237px;width:104px;height:30px;border-radius:15px;background:#dcdcdc;display:flex;align-items:center;justify-content:center;gap:8px}
.dots i{width:12px;height:12px;border-radius:50%;background:#999}
.dots i.on{background:var(--blue)}
h2{font-size:20px;font-weight:700;color:var(--heading)}
h2 span{color:var(--link)}
.copy p{font-size:13px;line-height:22px;margin-top:8px}
.copy a{color:var(--link);text-decoration:none}
.welcome{left:100px;top:498px;width:624px}
.welcome h2{margin-bottom:12px}
.divider{left:97px;top:774px;width:630px;height:1px;background:var(--line)}
.why{left:100px;top:794px;width:428px;text-align:justify}
.why h2{margin-bottom:12px;text-align:left}
.phone-art{left:552px;top:836px;width:172px;height:128px;border-radius:10px;background:linear-gradient(135deg,#4a5560,#9aa5b0 50%,#2f5fb0)}
.sidebar{left:755px;top:478px;width:302px;height:552px;background:linear-gradient(90deg,#ececec,#fafafa 8%,#fafafa)}
.qc-title{left:772px;top:498px;display:flex;align-items:center;gap:10px;font-size:18px;font-weight:700;color:var(--link)}
.qc-line{left:757px;top:540px;width:300px;height:1px;background:var(--line)}
.field{left:770px;width:279px;height:35px;border:1px solid var(--field);background:linear-gradient(#fff 70%,#f1f1f1);font-size:13px;color:#777;padding:10px 15px}
.field.msg{height:84px}
.captcha{left:770px;top:855px;width:279px;height:111px;background:var(--red);border-radius:6px;padding:4px}
.captcha-words{height:54px;background:linear-gradient(#fff,#ededed);border-radius:3px}
.captcha-input{position:absolute;left:8px;top:62px;width:150px;height:40px;background:#f7e7a6;border-radius:2px;font-size:9px;color:#333;padding:3px 16px}
.captcha-input span{display:block;margin-top:2px;height:20px;background:#fff;border:1px solid #6a8fc0}
.captcha-tools{position:absolute;left:164px;top:62px;width:20px;height:40px;background:#b51818;border-radius:2px}
.captcha-badge{position:absolute;left:190px;top:64px;width:26px;height:26px;border-radius:50%;border:3px solid #fff}
.submit{left:970px;top:979px;width:79px;height:31px;border-radius:4px;background:linear-gradient(#666,#2b2b2b);color:#fff;font-size:13px;font-weight:700;display:flex;align-items:center;justify-content:center}
.doc{top:1035px;height:36px;border-radius:18px;background:linear-gradient(#666,#2e2e2e);color:#fff;font-size:14px;font-weight:700;display:flex;align-items:center;padding-left:22px;gap:14px;box-shadow:0 1px 2px rgba(0,0,0,.4)}
.doc i{width:20px;height:20px;background:#e6e6e6;border-radius:2px}
.footer-links{left:86px;top:1106px;font-size:13px;color:#555;word-spacing:2px}
.footer-links span{margin:0 9px;color:#777}
.copyright{left:86px;top:1136px;font-size:13px;color:#555}
.social{left:1012px;top:1119px;display:flex;gap:6px}
.social i{width:23px;height:23px;border-radius:3px;background:#3b5a98}
.social i+i{background:#4aa7dc}
</style>
</head>
<body>
<div class="stage">
  <div class="abs band"></div>

  <header class="abs header"></header>
  <div class="abs brand"><span class="brand-mark"></span><span class="brand-name">QuorvanLabs</span></div>
  <div class="abs contact-btn">
    <svg width="50" height="40" viewBox="0 0 50 40"><circle cx="22" cy="20" r="18" fill="#ddd"/><path d="M14 12c2-2 4-2 5 0l2 4c0 2-2 2-2 3 1 3 3 5 6 6 1 0 1-2 3-2l4 2c2 1 2 3 0 5-6 4-22-8-18-18z" fill="#1a5ea8"/></svg>
    CONTACT US
  </div>
  <div class="abs callus">CALL US : <b>1.888.555.0142</b> &nbsp; | &nbsp; E-MAIL : <a>info@quorvanlabs.example</a></div>

  <nav class="abs nav">
    <a class="active">HOME</a><a>ABOUT US</a><a>TELEPHONE VOIP SOLUTIONS</a><a>IP, LAN AND INTERNET</a><a>SUPPORT</a><a>CONTACT US</a>
  </nav>

  <div class="abs main"></div>

  <section class="abs slider">
    <div class="abs slide-photo" role="img" aria-label="Smiling support agent wearing a headset"></div>
    <div class="abs slide-art" role="img" aria-label="VoIP lettering with a globe and computer mouse"></div>
    <p class="abs slide-text">QuorvanLabs provides complete telephone VoIP<br>PBX solutions for businesses large and small.</p>
    <div class="abs dots"><i class="on"></i><i></i><i></i><i></i></div>
  </section>

  <section class="abs welcome copy">
    <h2>Welcome to <span>QuorvanLabs</span></h2>
    <p>Our team of telecom engineers will design and install the best business telephone VoIP PBX solution for your requirements.&nbsp; System features include: standard and advanced PBX call control actions, video telephone calling, toll free calling any where in the world, and 24x7 support.</p>
    <p>For more details, <a>click here</a></p>
    <p>We also provide complete wired and wireless LAN/WAN/IP solutions and services for data, voice, Internet and private intranet networks to a variety of industries, including hospitality, industrial, commercial and institutional groups.</p>
    <p>Our Support Services Division call center provides 24 x 7 help desk technical support services for industries including telecommunications, commercial and lodging / hotel.</p>
  </section>
  <div class="abs divider"></div>

  <section class="abs why copy">
    <h2>Why <span>QuorvanLabs?</span></h2>
    <p>QuorvanLabs provides state of the art VoIP PBX phone solutions with products tailored to small, medium, and large businesses. Our engineering team will asses your communication requirements and provide you with the best designed solution for your business needs.</p>
    <p>QuorvanLabs will be there for you during the whole process. From the initial quote all the way through installation and support. QuorvanLabs is committed to you!</p>
  </section>
  <div class="abs phone-art" role="img" aria-label="Desk IP phone with a blue network cable"></div>

  <aside class="abs sidebar"></aside>
  <div class="abs qc-title">
    <svg width="24" height="24" viewBox="0 0 24 24"><rect x="3" y="3" width="16" height="19" fill="#fff" stroke="#999"/><path d="M6 8h10M6 12h10M6 16h7" stroke="#bbb"/><path d="M14 18l8-10" stroke="#c8a040" stroke-width="2"/></svg>
    Quick Contact
  </div>
  <div class="abs qc-line"></div>
  <div class="abs field" style="top:558px">Name</div>
  <div class="abs field" style="top:608px">Company</div>
  <div class="abs field" style="top:658px">Phone</div>
  <div class="abs field" style="top:708px">Email</div>
  <div class="abs field msg" style="top:758px">Message</div>
  <div class="abs captcha">
    <div class="captcha-words" role="img" aria-label="Distorted verification words"></div>
    <div class="captcha-input">Type the two words:<span></span></div>
    <div class="captcha-tools"></div>
    <div class="captcha-badge"></div>
  </div>
  <div class="abs submit">SUBMIT</div>

  <div class="abs doc" style="left:95px;width:298px"><i></i>Norvix's Callvane Feature Page</div>
  <div class="abs doc" style="left:405px;width:269px"><i></i>Norvix's HD Voice IP Phones</div>
  <div class="abs doc" style="left:687px;width:369px"><i></i>Halden's Veranta B410 IP Phone - datasheet</div>

  <footer>
    <div class="abs footer-links">Home<span>|</span>About us<span>|</span>Telephone VOIP Solutions<span>|</span>IP, LAN and Internet<span>|</span>Support<span>|</span>Contact us</div>
    <div class="abs copyright">Copyright &nbsp;©&nbsp; 2013 &nbsp; www.quorvanlabs.example &nbsp;&nbsp; All rights reserved.</div>
    <div class="abs social"><i></i><i></i></div>
  </footer>
</div>
</body>
</html>
```